Newspaper AD in the Restaurant Section HOMECARE/Senior Living

Looking for an ad that is 6.425 inches wide and 5 inches tall to go into the newspaper weekly it will be in the restaurant section. We are a senior homecare company and we are looking to show clients that caregivers are able to assist them not only in personal care needs but also meal prep. We would like the design to have the feel of our existing ad or our newly launched website. It will be in the Savor section of the Pacific Morning Ledger which is not where we normally would advertise as a homecare agency so ad has to have some kind of feel for that section.
It should say somewhere maybe by contact info Call today for FREE Consultation.

Target Market(s)

Target market is Men/Women ages 35-105

Industry/Entity Type

Homecare and Senior Living

Font styles to use
Sans Serif

Colors
0054AA
0677BA
7BADD7
CADEEF
E8F1F8
FFF300
FFF600
FEFA6F
FFFEC7
FFFEE8
EB3D1F
EC4F4E
F09395
F8D3D4
FCEDEE

Requirements
Must have
• Logo, Contact info: Phone number (808) 555-0173, email address Info@brightmeadowcare.com and website www.Brightmeadowcare.com.
Nice to have
• Something that will be eye catching and to the point. Maybe a picture of a caregiver preparing a meal with an elderly person

```html
<!DOCTYPE html>
<html lang="en">
<head>
<meta charset="utf-8">
<title>Bright Meadow Homecare – Newspaper Ad</title>
<link href="https://fonts.googleapis.com/css2?family=Montserrat:wght@300;500;600&family=Roboto+Condensed:wght@400;700&family=Oswald:wght@600&display=swap" rel="stylesheet">
<style>
  :root {
    --page-bg: #ececec;
    --ad-dark: #2a2829;
    --ad-dark-soft: #4a4647;
    --white: #ffffff;
    --ink: #1d1d1d;
    --teal: #0c6b5d;
    --coral: #e9775b;
    --coral-deep: #ee6a3f;
    --peach: #f6c2a6;
  }
  * { margin: 0; padding: 0; box-sizing: border-box; }
  html, body { width: 786px; height: 1200px; overflow: hidden; background: var(--page-bg); }

  .ad {
    position: absolute; left: 33px; top: 321px;
    width: 720px; height: 558px;
    background: var(--ad-dark);
    overflow: hidden;
    box-shadow: 0 6px 18px rgba(0,0,0,.35);
  }
  .ad__backdrop {
    position: absolute; inset: 0;
    background:
      radial-gradient(ellipse 260px 320px at 640px 150px, rgba(120,112,110,.45), transparent 70%),
      radial-gradient(ellipse 380px 220px at 430px 430px, rgba(90,84,84,.5), transparent 70%),
      linear-gradient(160deg, var(--ad-dark-soft), var(--ad-dark) 60%);
  }
  .ad__panel {
    position: absolute; left: 0; top: 0; width: 496px; height: 330px;
    background: var(--white);
  }

  .cta { position: absolute; left: 40px; top: 47px; color: var(--ink); }
  .cta__line {
    font-family: "Roboto Condensed", sans-serif; font-weight: 400;
    font-size: 23px; line-height: 24px; letter-spacing: .2px;
  }
  .cta__phone {
    display: flex; align-items: center; gap: 8px; margin-top: 12px;
    font-family: "Roboto Condensed", sans-serif; font-weight: 700; font-size: 27px;
  }
  .divider { position: absolute; left: 269px; top: 34px; width: 2px; height: 102px; background: var(--teal); }

  .offer { position: absolute; left: 286px; top: 38px; width: 194px; text-align: right; }
  .offer__title {
    font-family: "Oswald", sans-serif; font-weight: 600; font-size: 34px;
    line-height: 40px; color: var(--teal); letter-spacing: .3px; white-space: nowrap;
  }
  .offer__sub {
    font-family: "Montserrat", sans-serif; font-weight: 500; font-size: 15px;
    line-height: 16px; color: var(--coral); margin-top: 6px;
  }

  .values { position: absolute; left: 524px; top: 37px; list-style: none; }
  .values li {
    display: flex; align-items: center; gap: 8px;
    font-family: "Montserrat", sans-serif; font-weight: 300; font-size: 23px;
    line-height: 29px; color: var(--white); letter-spacing: .5px; white-space: nowrap;
  }

  .brand { position: absolute; left: 531px; top: 170px; width: 150px; text-align: center; color: var(--white); }
  .brand__mark { width: 40px; height: 40px; margin: 0 auto 12px; background: var(--coral); border-radius: 6px; }
  .brand__name {
    font-family: "Montserrat", sans-serif; font-weight: 500; font-size: 22px; line-height: 26px;
  }
  .brand__name span { display: block; font-size: 13px; letter-spacing: 4px; margin-top: 4px; }

  .photo-frame {
    position: absolute; left: 27px; top: 158px; width: 478px; height: 205px;
    background: var(--white); border-radius: 30px; padding: 7px;
    box-shadow: 0 2px 6px rgba(0,0,0,.25);
  }
  .photo-frame__image {
    width: 100%; height: 100%; border-radius: 24px;
    background: linear-gradient(100deg, #b78a5a 0%, #d9c79a 30%, #3f7fc0 48%, #4fb4d6 62%, #e8e2cf 82%, #c9d6c4 100%);
  }

  .quote {
    position: absolute; left: 0; top: 394px; width: 504px; text-align: center;
    font-family: "Roboto Condensed", sans-serif; font-weight: 400; font-size: 26px; line-height: 27px;
    white-space: nowrap;
  }
  .quote__l1 { color: var(--white); }
  .quote__l2 { color: var(--peach); }
  .quote__l3 { color: var(--coral-deep); }

  .contact {
    position: absolute; top: 507px; display: flex; align-items: center; gap: 7px;
    font-family: "Roboto Condensed", sans-serif; font-weight: 700; font-size: 14px;
    color: var(--white); text-transform: uppercase; white-space: nowrap;
  }
  .contact--web { left: 44px; }
  .contact--mail { left: 292px; }
</style>
</head>
<body>
<main class="ad">
  <div class="ad__backdrop" role="img" aria-label="Faded dark photo of a caregiver serving a meal at a table"></div>
  <div class="ad__panel"></div>

  <div class="cta">
    <p class="cta__line">CALL TODAY FOR</p>
    <p class="cta__line">FREE CONSULTATION.</p>
    <p class="cta__phone">
      <svg width="30" height="30" viewBox="0 0 30 30" aria-hidden="true">
        <circle cx="15" cy="15" r="13.5" fill="none" stroke="#1d1d1d" stroke-width="2"/>
        <path d="M10 8.5c1-.8 2-.6 2.6.4l1.2 2.2c.4.8.2 1.6-.5 2.1l-.8.6c.8 1.8 2.1 3.2 3.9 4.1l.6-.8c.5-.7 1.4-.9 2.1-.5l2.2 1.2c1 .6 1.2 1.6.4 2.6-1.4 1.8-3.4 1.9-5.6.7-3.2-1.8-5.4-4.3-6.6-7.6-.7-2-.5-3.7.5-5z" fill="none" stroke="#1d1d1d" stroke-width="1.6"/>
      </svg>
      (808) 555-0173
    </p>
  </div>

  <div class="divider"></div>

  <div class="offer">
    <h1 class="offer__title">WE PROVIDE</h1>
    <p class="offer__sub">RESIDENTIAL<br>CARE THAT<br>PROMOTES</p>
  </div>

  <ul class="values">
    <li><svg width="18" height="18" viewBox="0 0 18 18" aria-hidden="true"><circle cx="9" cy="9" r="9" fill="#fff"/><path d="M5 9.3l2.6 2.5L13 6.3" fill="none" stroke="#2a2829" stroke-width="2.2"/></svg>well-being,</li>
    <li><svg width="18" height="18" viewBox="0 0 18 18" aria-hidden="true"><circle cx="9" cy="9" r="9" fill="#fff"/><path d="M5 9.3l2.6 2.5L13 6.3" fill="none" stroke="#2a2829" stroke-width="2.2"/></svg>connection,</li>
    <li><svg width="18" height="18" viewBox="0 0 18 18" aria-hidden="true"><circle cx="9" cy="9" r="9" fill="#fff"/><path d="M5 9.3l2.6 2.5L13 6.3" fill="none" stroke="#2a2829" stroke-width="2.2"/></svg>dignity</li>
  </ul>

  <div class="brand">
    <div class="brand__mark"></div>
    <p class="brand__name">Bright Meadow<span>HOMECARE</span></p>
  </div>

  <figure class="photo-frame">
    <div class="photo-frame__image" role="img" aria-label="Caregiver in blue scrubs laughing with a senior woman on a sofa in a bright living room"></div>
  </figure>

  <blockquote class="quote">
    <p class="quote__l1">CAREGIVING IS A SERIES</p>
    <p class="quote__l2">OF SMALL ACTS OF CARE THAT</p>
    <p class="quote__l3">ALTER THE COURSE OF SOMEONE'S LIFE."</p>
  </blockquote>

  <p class="contact contact--web">
    <svg width="17" height="17" viewBox="0 0 18 18" aria-hidden="true" fill="none" stroke="#fff" stroke-width="1.3"><circle cx="9" cy="9" r="8"/><ellipse cx="9" cy="9" rx="3.5" ry="8"/><path d="M1 9h16M2.5 5h13M2.5 13h13"/></svg>
    www.Brightmeadowcare.com
  </p>
  <p class="contact contact--mail">
    <svg width="17" height="17" viewBox="0 0 18 18" aria-hidden="true" fill="none" stroke="#fff" stroke-width="1.3"><circle cx="9" cy="9" r="8"/><rect x="4.5" y="6" width="9" height="6.5"/><path d="M4.5 6L9 10l4.5-4"/></svg>
    Info@brightmeadowcare.com
  </p>
</main>
</body>
</html>
```